Business Card Design for Cybersecurity Company - Quorvent Systems

We need a business card design for our new cybersecurity company, Quorvent. We’re going for a clean, hi tech look that feels modern, premium, and trustworthy. We want a design that really stands out and makes people say WOW when we hand it over!

Quorvent delivers reliable IT support and managed services for small and mid sized businesses. We help companies stay secure, efficient, and connected through proactive monitoring, cybersecurity services, cloud management, and remote support.

Target Market(s)

Designers should target small and mid sized businesses that need dependable cybersecurity and IT support.

Industry/Entity Type

Cybersecurity, Managed Service Provider, IT services

Contact Information for Business Card

Contact information

Requirements
Must have
• The card should look clean, modern, and tech focused, with the Quorvent logo, clear contact info, and strong readability. It needs to feel premium and professional while still keeping a simple layout that fits a cybersecurity and IT brand.
Nice to have
• Nice to have elements include subtle touches that give the card a modern, tech feel, along with a layout that works well in different background styles.
Should not have
• The card should avoid clutter, loud graphics, or anything that takes attention away from the logo and contact details.

```html
<!DOCTYPE html>
<html lang="en">
<head>
<meta charset="utf-8">
<title>Quorvent Systems – Business Cards</title>
<link href="https://fonts.googleapis.com/css2?family=Montserrat:wght@700&family=Open+Sans:wght@400;600&display=swap" rel="stylesheet">
<style>
  :root {
    --stage: #1f1f22;
    --violet: #6b2bd9;
    --blue: #3461ef;
    --ring: #3a55e8;
    --white: #ffffff;
    --ink-logo: #4a3fe0;
  }
  * { margin: 0; padding: 0; box-sizing: border-box; }
  html, body {
    width: 1200px; height: 1015px; overflow: hidden;
    background: var(--stage);
    font-family: "Open Sans", Arial, sans-serif;
  }
  .stage {
    position: relative; width: 1200px; height: 1015px;
    display: flex; flex-direction: column; align-items: center; justify-content: center; gap: 55px;
  }
  .card {
    position: relative; width: 700px; height: 400px; overflow: hidden;
    background: linear-gradient(160deg, var(--violet) 0%, var(--blue) 75%);
    box-shadow: 0 18px 40px rgba(0,0,0,.55);
  }
  /* Back card */
  .card-back .brand {
    position: absolute; left: 60px; bottom: 60px;
    display: flex; align-items: center; gap: 16px;
  }
  .brand-dot {
    width: 44px; height: 44px; border-radius: 50%;
    border: 3px solid var(--white);
  }
  .brand-name {
    font-family: "Open Sans", Arial, sans-serif; font-weight: 600;
    font-size: 34px; color: var(--white); letter-spacing: .5px;
  }
  /* Front card */
  .front-disc {
    position: absolute; left: 400px; top: -70px; width: 430px; height: 430px;
    border-radius: 50%; background: var(--white);
    box-shadow: -14px 6px 0 0 var(--ring);
  }
  .card-front .brand {
    position: absolute; left: 450px; top: 120px; width: 230px;
    display: flex; flex-direction: column; align-items: center; gap: 14px;
  }
  .card-front .brand-dot { border-color: var(--ink-logo); width: 56px; height: 56px; }
  .card-front .brand-name { color: var(--ink-logo); font-size: 30px; text-align: center; line-height: 1.15; }
  .identity { position: absolute; left: 48px; top: 62px; color: var(--white); }
  .person-name { font-family: "Montserrat", Arial, sans-serif; font-weight: 700; font-size: 30px; }
  .person-role, .person-company { font-size: 17px; line-height: 1.35; }
  .person-role { margin-top: 4px; }
  .contact-list {
    position: absolute; left: 48px; bottom: 40px; list-style: none; color: var(--white);
    font-size: 17px;
  }
  .contact-list li { display: flex; align-items: center; gap: 12px; line-height: 29px; }
  .contact-list svg { width: 18px; height: 18px; fill: none; stroke: var(--white); stroke-width: 1.8; }
</style>
</head>
<body>
<main class="stage">
  <section class="card card-back" aria-label="Card back">
    <div class="brand">
      <span class="brand-dot"></span>
      <span class="brand-name">Quorvent Systems</span>
    </div>
  </section>

  <section class="card card-front" aria-label="Card front">
    <div class="front-disc"></div>
    <div class="brand">
      <span class="brand-dot"></span>
      <span class="brand-name">Quorvent Systems</span>
    </div>
    <div class="identity">
      <h1 class="person-name">Dana Merrick</h1>
      <p class="person-role">Owner | CEO</p>
      <p class="person-company">Quorvent Systems</p>
    </div>
    <ul class="contact-list">
      <li><svg viewBox="0 0 24 24"><path d="M5 3h4l2 5-3 2a11 11 0 0 0 6 6l2-3 5 2v4a2 2 0 0 1-2 2A17 17 0 0 1 3 5a2 2 0 0 1 2-2z"/></svg>(855) 555-0142</li>
      <li><svg viewBox="0 0 24 24"><rect x="7" y="2" width="10" height="20" rx="2"/><line x1="11" y1="18" x2="13" y2="18"/></svg>(813) 555-0187</li>
      <li><svg viewBox="0 0 24 24"><rect x="3" y="5" width="18" height="14"/><path d="M3 5l9 8 9-8"/></svg>dana@quorvent.com</li>
      <li><svg viewBox="0 0 24 24"><circle cx="12" cy="12" r="9"/><path d="M3 12h18M12 3c3 3 3 15 0 18M12 3c-3 3-3 15 0 18"/></svg>www.quorvent.com</li>
    </ul>
  </section>
</main>
</body>
</html>
```